Harbor of Mercy - Team of Rabbis and Doctors Helping Families Dealing with Illness

The Harbor of Mercy is an organization that accompanies families dealing with severe illnesses of a family member. A team of rabbis and doctors provide support and real-time responses to these families.
The site theme is medicine and law, but the target market is religious Jewish families in crisis. Thus, the site design needs to combine:
- professional, conservative, serious
- spiritual
- warm hug

Target Market(s)

religious families suffering a health crisis

Industry/Entity Type

Non-profit organization

Number of Pages Required

1 page

Font styles to use
Sans Serif

Requirements
Must have
• Final design in PSD format. List of fonts used, colors used and link/button colors used in the design.

```html
<!DOCTYPE html>
<html lang="en">
<head>
<meta charset="utf-8">
<title>Harbor of Mercy</title>
<link href="https://fonts.googleapis.com/css2?family=Raleway:wght@500;600;700;800&family=Montserrat:wght@400;500;600&display=swap" rel="stylesheet">
<style>
:root{
  --dark:#1c3535;
  --teal:#14a8a6;
  --cream:#fdfbf5;
  --beige:#eee8dd;
  --ink:#1f2a2a;
  --muted:#6d7474;
  --light:#ffffff;
}
*{margin:0;padding:0;box-sizing:border-box}
html,body{width:1200px;height:3847px;overflow:hidden}
body{position:relative;background:var(--cream);font-family:"Montserrat",sans-serif;color:var(--ink)}
.abs{position:absolute}
.h{font-family:"Raleway",sans-serif;font-weight:800;letter-spacing:4px;color:var(--ink)}
.bar{position:absolute;left:0;width:1200px}
.underline{display:block;width:18px;height:2px;background:var(--teal);margin-top:6px}
.btn{position:absolute;background:var(--teal);color:#fff;font-family:"Raleway",sans-serif;font-weight:700;font-size:12px;letter-spacing:1.5px;display:flex;align-items:center;justify-content:center}
.ph{position:absolute}
/* top bar */
.topbar{top:0;height:30px;background:var(--dark);color:#d9e3e2;font-size:10px}
.topbar span{position:absolute;top:9px;display:flex;align-items:center;gap:6px}
.dot{width:12px;height:12px;border-radius:50%;background:#d9e3e2;display:inline-block}
/* nav */
.nav{top:30px;height:72px;background:var(--cream);border-bottom:1px solid #ece7da}
.nav a{position:absolute;top:32px;font-size:11px;font-weight:600;color:var(--ink);text-decoration:none;font-family:"Raleway",sans-serif}
.nav a.active{color:var(--teal);text-decoration:underline}
.brand{position:absolute;left:830px;top:22px;display:flex;align-items:center;gap:8px;font-family:"Raleway",sans-serif;font-weight:800;font-size:17px;color:#e08a2c}
.brand i{width:16px;height:16px;background:var(--teal);display:block}
/* hero */
.hero{top:104px;height:508px;background:linear-gradient(90deg,#fbfbfb 0%,#f2f1ee 22%,#c9c6bf 45%,#a9a59c 65%,#e3e4e4 85%,#cfd1d0 100%)}
.hero h1{position:absolute;left:231px;top:258px;font-family:"Raleway",sans-serif;font-weight:800;font-size:32px;letter-spacing:4px;line-height:35px;color:var(--ink)}
.hero h1 em{font-style:normal;color:var(--teal)}
.dots span{position:absolute;top:570px;width:12px;height:12px;border-radius:50%;background:#eef0ef}
/* about */
.about-txt{left:660px;top:785px;width:300px;font-size:11.5px;line-height:19px;letter-spacing:1px;color:#555}
/* questions */
.questions{top:1062px;height:508px;background:var(--dark)}
.q-title{top:1106px;width:1200px;text-align:center;color:#fff;font-size:25px}
.q-title .underline{margin:6px auto 0 395px}
/* services */
.card{position:absolute;top:1697px;width:176px;height:360px;background:var(--dark);border-radius:3px;overflow:hidden}
.card .img{height:193px}
.card h3{font-family:"Raleway",sans-serif;font-weight:700;font-size:14px;color:#fff;margin:16px 12px 8px}
.card p{font-size:11px;line-height:18px;color:#cfd9d8;margin:0 13px;height:78px}
.card a{display:block;font-size:10.5px;color:var(--teal);margin:10px 13px;font-weight:600}
/* testimonials */
.testi{top:2145px;height:374px;background:var(--beige)}
/* articles */
.art{position:absolute;top:2622px;width:239px;height:373px;background:#fff;box-shadow:0 3px 12px rgba(0,0,0,.08)}
.art .img{height:217px}
.art h3{font-family:"Raleway",sans-serif;font-weight:700;font-size:15px;letter-spacing:1.5px;margin:16px 19px 6px;line-height:16px;height:32px}
.art .date{font-size:10px;color:#b9bcbc;margin:0 19px 6px}
.art p{font-size:11px;line-height:16px;color:#777;margin:0 19px;height:52px}
.art a{display:block;font-size:11px;color:var(--teal);font-weight:600;margin:4px 19px}
/* ask */
.ask{top:3122px;height:418px;background:var(--beige)}
.label{position:absolute;left:230px;font-size:11px}
.field{position:absolute;left:306px;width:312px;background:#fff;border:1px solid #ddd;font-size:11px;color:#bbb;padding:8px 14px}
/* footer */
.footer{top:3540px;height:307px;background:var(--dark);color:#fff}
.fcontact{position:absolute;left:231px;display:flex;align-items:center;gap:14px;font-size:11px;line-height:14px}
.fcontact i{width:18px;height:18px;border-radius:50%;background:#e6ecec;display:block}
.flinks a{position:absolute;left:497px;font-size:11px;font-weight:600;color:#fff;text-decoration:none}
.ftitle{position:absolute;top:3626px;font-family:"Raleway",sans-serif;font-weight:700;font-size:14px;letter-spacing:3px;color:#7b9190}
</style>
</head>
<body>

<div class="bar topbar">
  <span style="left:231px"><svg width="13" height="13" viewBox="0 0 13 13"><circle cx="5.5" cy="5.5" r="4" fill="none" stroke="#d9e3e2" stroke-width="1.6"/><line x1="8.5" y1="8.5" x2="12" y2="12" stroke="#d9e3e2" stroke-width="1.6"/></svg>Search</span>
  <span style="left:328px"><i class="dot"></i>Community Page &nbsp;|</span>
  <span style="left:445px"><i class="dot"></i>info@harborofmercy.org &nbsp;|</span>
  <span style="left:585px"><i class="dot"></i>+4 124 555 010</span>
  <span style="left:788px">Dedication 1</span>
  <span style="left:874px">|</span>
  <span style="left:902px">Dedication 2</span>
</div>

<nav class="bar nav">
  <a class="active" style="left:231px">Home</a>
  <a style="left:301px">Services ▾</a>
  <a style="left:388px">Testimonials</a>
  <a style="left:497px">Blog ▾</a>
  <a style="left:561px">About Us</a>
  <a style="left:652px">Contact Us</a>
  <div class="brand"><i></i>Harbor of Mercy</div>
</nav>

<section class="bar hero">
  <div class="ph" role="img" aria-label="Doctor in a white coat sitting with a young patient on a sofa" style="left:0;top:0;width:1200px;height:508px"></div>
</section>
<h1 class="hero-h" style="position:absolute;left:231px;top:258px;font-family:'Raleway',sans-serif;font-weight:800;font-size:31px;letter-spacing:4px;line-height:35px;color:var(--ink)">Should Cancer Patients<br><span style="color:var(--teal)">Continue Treatment?</span></h1>
<div class="btn" style="left:231px;top:346px;width:128px;height:30px">Read More</div>
<div class="dots"><span style="left:572px"></span><span style="left:594px;background:var(--teal)"></span><span style="left:616px"></span></div>

<div class="ph" role="img" aria-label="Grandfather reading a book to his family, with a play button" style="left:231px;top:706px;width:399px;height:257px;background:linear-gradient(135deg,#2a3b4e,#52606c 50%,#3a4654);border-radius:3px"></div>
<svg class="abs" style="left:401px;top:806px" width="58" height="58" viewBox="0 0 58 58"><circle cx="29" cy="29" r="26" fill="none" stroke="#fff" stroke-width="2.5"/><path d="M23 18 L40 29 L23 40 Z" fill="none" stroke="#fff" stroke-width="2.5" stroke-linejoin="round"/></svg>
<div class="abs h" style="left:660px;top:736px;font-size:25px">ABOUT US<span class="underline"></span></div>
<p class="abs about-txt">Lorem ipsum dolor sit amet, consectetur adi piscing elit, sed do eiusmod tempor incidi dunt ut labore et dolore magna aliqua. Quis ipsum suspendisse ultrices gravida. Risus commodo viverra maecenas accumsan lacus vel facilisis.</p>
<div class="btn" style="left:660px;top:909px;width:128px;height:30px">Learn More</div>

<section class="bar questions"></section>
<div class="abs h q-title">QUESTIONS YOU MAY HAVE<span class="underline"></span></div>
<div class="abs" style="left:230px;top:1230px;font-family:'Raleway',sans-serif;font-weight:600;font-size:24px;letter-spacing:2.5px;line-height:28px;color:#fff">Should morphine be<br>given to the patient?</div>
<p class="abs" style="left:230px;top:1310px;width:320px;font-size:11.5px;line-height:19px;letter-spacing:1px;color:#dbe3e2">Dolor sit amet, consectetur adipiscing elit, sed do eiusmod tempor incidi dunt ut labore et dolore magna aliqua. Quis ipsum su spen disse ultrices gravida. Risus commodo viverra maecenas accumsan lacus vel facilisis.</p>
<svg class="abs" style="left:230px;top:1426px" width="80" height="14" viewBox="0 0 80 14"><path d="M24 7H2M8 1L2 7l6 6" fill="none" stroke="#51706f" stroke-width="1.5"/><path d="M50 7h22M66 1l6 6-6 6" fill="none" stroke="#fff" stroke-width="1.5"/></svg>
<div class="ph" role="img" aria-label="Rabbi reading by lamplight" style="left:606px;top:1173px;width:463px;height:317px;background:radial-gradient(circle at 25% 20%,#d49a5c,#6b4226 45%,#2a1a10 90%);border-radius:3px"></div>

<div class="abs h" style="left:0;top:1641px;width:1200px;text-align:center;font-size:25px">OUR SERVICES<span class="underline" style="margin-left:490px"></span></div>
<div class="card" style="left:231px"><div class="img" role="img" aria-label="Elder teaching young students" style="background:linear-gradient(135deg,#3b3f44,#8b8781)"></div><h3>Course</h3><p>Lorem ipsum dolor sit, consectetur adipiscing elit, sed do eiusmod tempor incidi dunt ut labore et</p><a>Learn More...</a></div>
<div class="card" style="left:418px"><div class="img" role="img" aria-label="Audience seated at a conference" style="background:linear-gradient(135deg,#4f5a68,#a0a8b2)"></div><h3>Conferences</h3><p>Sit amet, consectetur adi piscing elit, sed do eiu smod tempor incidi dunt ut labore et dolore magna</p><a>Learn More...</a></div>
<div class="card" style="left:606px"><div class="img" role="img" aria-label="Hand resting on an open book" style="background:linear-gradient(135deg,#6a4a3a,#d8c7ac)"></div><h3>Lectures</h3><p>Lorem ipsum dolor sit met, cons ectetur adi pi scing elit, sed do eiusmod</p><a>Learn More...</a></div>
<div class="card" style="left:792px"><div class="img" role="img" aria-label="Man in prayer shawl reading by candlelight" style="background:linear-gradient(135deg,#1e1812,#7a5a36)"></div><h3>Hotline</h3><p>Ced do eiusmod tempor incidi dunt ut labore et dolore magna aliqua. Qpsum suspendisse</p><a>Contact...</a></div>

<section class="bar testi"></section>
<div class="abs h" style="left:0;top:2190px;width:1200px;text-align:center;font-size:25px">TESTIMONIALS<span class="underline" style="margin-left:488px"></span></div>
<svg class="abs" style="left:578px;top:2236px" width="46" height="36" viewBox="0 0 46 36"><path d="M2 36V20C2 8 8 2 18 0v6c-6 2-8 6-8 12h8v18zM26 36V20c0-12 6-18 16-20v6c-6 2-8 6-8 12h8v18z" fill="#d9d2c5"/></svg>
<p class="abs" style="left:420px;top:2288px;width:360px;text-align:center;font-size:11px;line-height:19.5px;font-style:italic;color:#444">"Lorem ipsum dolor sit amet, consectetur adipiscing elit, sed do eiusmod tempor in cididunt ut labore et dolore magna aliqua. Quis ipsum suspendisse ultrices gravida. Risus commodo viverra maecenas accum san lacus vel facilisis"</p>
<svg class="abs" style="left:306px;top:2309px" width="600" height="14" viewBox="0 0 600 14"><path d="M24 7H2M8 1L2 7l6 6" fill="none" stroke="#14a8a6" stroke-width="1.6"/><path d="M568 7h22M584 1l6 6-6 6" fill="none" stroke="#14a8a6" stroke-width="1.6"/></svg>
<div class="abs" style="left:0;top:2380px;width:1200px;text-align:center;font-size:11px;line-height:19px;color:#a9a79f">Leah R.<br>Sep 2023</div>
<div class="btn" style="left:522px;top:2440px;width:156px;height:30px;font-size:11px;letter-spacing:.5px">View Testimonials</div>

<div class="abs h" style="left:227px;top:2570px;font-size:25px">LATEST ARTICLES<span class="underline"></span></div>
<div class="art" style="left:227px"><div class="img" role="img" aria-label="Family gathered around candles at a table" style="background:linear-gradient(135deg,#1f1a16,#6e5640)"></div><h3>Finding Answers In Times of Crises</h3><div class="date">12 Dec 2023</div><p>Sit amet, consectetur adi piscing elit, sed do eiu smod tempor incidi dunt ut labore et dolore</p><a>Continue Reading...</a></div>
<div class="art" style="left:478px"><div class="img" role="img" aria-label="Hands lighting candles on a menorah" style="background:linear-gradient(135deg,#5b8a8c,#e2cfa8)"></div><h3>Dolor Sit Amet</h3><div class="date">07 Dec 2023</div><p>Consectetur adi piscing elit, sed do eiu smod tempor incidi dunt ut labore et dolore magna</p><a>Continue Reading...</a></div>
<div class="art" style="left:727px"><div class="img" role="img" aria-label="Young man studying among stacks of books" style="background:linear-gradient(135deg,#7a3a2a,#c9b79a)"></div><h3>Tempor Sed</h3><div class="date">02 Dec 2023</div><p>Eiusmod tempor incidi dunt ut labore et dolore magna aliqua. ipsum suspendisse ultrices</p><a>Continue Reading...</a></div>
<div class="abs" style="left:507px;top:3039px;width:175px;height:31px;border:1.5px solid var(--teal);color:var(--teal);font-family:'Raleway',sans-serif;font-weight:700;font-size:11px;letter-spacing:1px;display:flex;align-items:center;justify-content:center">Browse All Articles</div>

<section class="bar ask"></section>
<div class="ph" role="img" aria-label="Rabbi reading a book by the seashore" style="left:627px;top:3122px;width:573px;height:418px;background:linear-gradient(90deg,#eee8dd 0%,#c7d6e4 25%,#9cb6cc 60%,#7f98ad 100%)"></div>
<div class="abs h" style="left:230px;top:3194px;font-size:25px">ASK THE RABBI</div>
<div class="abs" style="left:230px;top:3227px;width:388px;height:1px;background:#d5cfc2"></div>
<p class="abs" style="left:230px;top:3233px;font-size:10.5px;line-height:18px;color:#444">For any questions or concerns, please get in touch with us.<br>We are available <b>24/7.</b></p>
<div class="label" style="top:3292px">Name*</div><div class="field" style="top:3283px;height:30px">Name</div>
<div class="label" style="top:3331px">Email*</div><div class="field" style="top:3322px;height:30px">Email Address</div>
<div class="label" style="top:3371px">Message*</div><div class="field" style="top:3363px;height:98px">Type your message here</div>
<div class="btn" style="left:306px;top:3473px;width:154px;height:30px;font-size:12px;letter-spacing:.5px">Submit ›</div>

<footer class="bar footer"></footer>
<div class="abs" style="left:231px;top:3590px;display:flex;align-items:center;gap:8px;font-family:'Raleway',sans-serif;font-weight:800;font-size:17px;color:#e08a2c"><i style="width:16px;height:16px;background:var(--teal);display:block"></i>Harbor of Mercy</div>
<div class="fcontact" style="top:3651px"><i></i><span>14 Cedar Lane<br>Jerusalem</span></div>
<div class="fcontact" style="top:3698px"><i></i><span>+4 124 555 010</span></div>
<div class="fcontact" style="top:3724px"><i></i><span>info@harborofmercy.org</span></div>
<div class="fcontact" style="top:3750px"><i></i><span>Community Page</span></div>
<div class="ftitle" style="left:497px">QUICK LINKS</div>
<div class="ftitle" style="left:716px">NEWSLETTER</div>
<div class="abs" style="left:497px;top:3640px;width:470px;height:1px;background:#3a5656"></div>
<div class="flinks">
  <a style="top:3655px">Home</a><a style="top:3680px">Services</a><a style="top:3705px">Testimonials</a><a style="top:3730px">Blog</a><a style="top:3755px">About Us</a><a style="top:3780px">Contact Us</a>
</div>
<p class="abs" style="left:716px;top:3655px;width:260px;font-size:11px;line-height:14px">Subscribe to our newsletter for the latest updates and articles</p>
<div class="abs" style="left:716px;top:3697px;width:156px;height:29px;background:#fff;font-size:10px;color:#bbb;padding:9px 14px">email address</div>
<div class="btn" style="left:872px;top:3697px;width:98px;height:29px;font-size:12px;letter-spacing:.3px">Subscribe ›</div>
<div class="abs" style="left:497px;top:3829px;font-size:8.5px;color:#7b9190">© 2023 All Rights Reserved &nbsp;|&nbsp; Harbor of Mercy</div>

</body>
</html>
```